Coach company requires modern brochure

We need a brochure designed that shows our various coach services. The aim of the brochure is to attract new business, therefore we need something that is modern, eye-catching and uses a lot of imagery/design rather than being text heavy.

I have all the images that can be sent via dropbox or google drive if you want to request them.

Target Market(s)

Wedding planners, event companies, school business managers, sporting groups

Industry/Entity Type

Tourism

Requirements
Must have
• 4 x a4 pages
• Bold and eye catching cover page

```html
<!DOCTYPE html>
<html lang="en">
<head>
<meta charset="utf-8">
<title>Ridgeway Coach Lines – Group Services</title>
<link href="https://fonts.googleapis.com/css2?family=Raleway:ital,wght@0,500;0,600;0,800;1,500&display=swap" rel="stylesheet">
<style>
  :root{
    --green:#2fb51f;
    --sky:#3fb3e2;
    --rule:#a9dcf2;
    --body:#4a4a4a;
    --quote:#34b02a;
    --page:#f4f6f6;
  }
  html,body{margin:0;padding:0;overflow:hidden;}
  body{width:848px;height:1200px;font-family:"Raleway",Arial,sans-serif;}
  .page{position:relative;width:848px;height:1200px;overflow:hidden;
    background:var(--page);}
  .backdrop{position:absolute;inset:0;
    background:linear-gradient(180deg,#eef1f1 0%,#e6ebec 30%,#f2f4f4 55%,#e3e9ec 75%,#eceff0 100%);}
  .band{position:absolute;left:0;width:848px;height:20px;background:var(--green);}
  .band--top{top:0;}
  .band--bottom{bottom:0;}
  .section-title{position:absolute;left:50px;margin:0;font-weight:800;font-size:29px;
    color:var(--sky);letter-spacing:.2px;line-height:1;}
  .section-copy{position:absolute;left:50px;margin:0;font-weight:600;font-size:14.6px;
    line-height:19.4px;color:var(--body);text-align:justify;}
  .photo{position:absolute;}
  .rule{position:absolute;left:50px;width:749px;height:1px;background:var(--rule);}
  .testimonial{position:absolute;left:50px;top:586px;width:750px;margin:0;
    font-style:italic;font-weight:500;font-size:17.6px;line-height:24.6px;
    color:var(--quote);text-align:justify;}
</style>
</head>
<body>
<div class="page">
  <div class="backdrop" role="img" aria-label="Faint background photo of palm trees and a sandy beach"></div>
  <div class="band band--top"></div>

  <h2 class="section-title" style="top:56px;">Corporate Groups</h2>
  <p class="section-copy" style="top:100px;width:356px;">Ridgeway Coach Lines can take some of the pressure off organising your next corporate event. With an extensive range of vehicles in our fleet, we can offer a reliable, punctual and professional service for all group sizes. We pride ourselves on our knowledge of corporate venues, and are the go to partner for a number of Event Planners across the Sunshine Coast.</p>
  <div class="photo" style="left:443px;top:57px;width:356px;height:201px;background:linear-gradient(160deg,#9fb8a4 0%,#5f7d5b 45%,#c9cbb9 100%);" role="img" aria-label="Photo of a corporate group in blue shirts beside a row of golf carts"></div>

  <div class="rule" style="top:295px;"></div>

  <h2 class="section-title" style="top:314px;">Educational Groups</h2>
  <p class="section-copy" style="top:357px;width:356px;">In addition to our regular school bus runs, we are also able to provide transport options for a wide range of other educational excursions. Be it day trips, school camps or sporting events, we can provide services for primary and secondary schools, as well as colleges and language schools. In addition to local schools, we can also provide Brisbane schools with a safe, reliable and great value transport option for camps on the Sunshine Coast.</p>
  <div class="photo" style="left:443px;top:316px;width:356px;height:265px;background:linear-gradient(150deg,#c7d6cc 0%,#6f8f67 40%,#8a7f74 75%,#b85a3c 100%);" role="img" aria-label="Photo of a tour group inside a greenhouse with tomato vines"></div>

  <p class="testimonial">‘This service has proven invaluable, and as this is a Community Event, we are sincerely grateful for the invaluable shuttle/transport service provided to our Festival (which is a not for profit organisation) by Ridgeway Coach Lines. It is due to their support, we continue to maintain a very cost effective ‘Community’ driven ticket price for families to attend this great event.’ Tom Fairweather, Festival Director, Bayside Long Weekend Festival</p>

  <div class="rule" style="top:743px;"></div>

  <h2 class="section-title" style="top:766px;">Sporting Groups</h2>
  <p class="section-copy" style="top:811px;width:749px;">Getting away with your team for a match or game and need some transport? We have an extensive fleet as well as spacious luggage trailers for your equipment, so let us know your dates and group size and we can easily organise your quote and booking.</p>
  <div class="photo" style="left:50px;top:887px;width:346px;height:258px;background:linear-gradient(180deg,#1c1f2a 0%,#3d3a44 35%,#2f8f3a 60%,#2a7d33 100%);" role="img" aria-label="Photo of a floodlit football stadium with a green pitch"></div>
  <div class="photo" style="left:410px;top:887px;width:389px;height:258px;background:linear-gradient(160deg,#0b3d8a 0%,#1c6fc4 45%,#3aa0e0 70%,#0a3478 100%);" role="img" aria-label="Photo of a swimmer doing freestyle in a pool lane"></div>

  <div class="band band--bottom"></div>
</div>
</body>
</html>
```